International Company needs a Letterhead & Envelope Design

Our Company name is Brightfold Harbor Limited.
We'd like to ask the Designers for the luxurious and sophisticated design. Our logo is very simple and neat with letter logos, so we look forward to more professional and refined designs from Designers.
We look forward to providing you with a great design.
Thanks very much in advance.

```html
<!DOCTYPE html>
<html lang="en">
<head>
<meta charset="utf-8">
<title>Brightfold Harbor Limited — Letterhead</title>
<link href="https://fonts.googleapis.com/css2?family=Lato:wght@400;700&family=Dancing+Script:wght@700&display=swap" rel="stylesheet">
<style>
  :root {
    --backdrop: #c6c7c9;
    --paper: #ffffff;
    --ink: #4a4a4a;
    --ink-soft: #555555;
    --rule: #9a9a9a;
    --band: #111111;
    --swoosh: #5c5c5c;
    --on-band: #ffffff;
  }
  * { box-sizing: border-box; margin: 0; padding: 0; }
  html, body {
    width: 1002px; height: 1200px; overflow: hidden;
    background: var(--backdrop);
    font-family: "Lato", Arial, sans-serif;
    color: var(--ink);
  }
  .letterhead {
    position: absolute; left: 82px; top: 59px;
    width: 835px; height: 1080px;
    background: var(--paper);
    box-shadow: 0 0 3px rgba(0,0,0,.18);
    overflow: hidden;
  }
  .brand {
    position: absolute; left: 70px; top: 20px;
    color: var(--ink-soft);
  }
  .brand-name {
    font-size: 35px; font-weight: 700; letter-spacing: 1px; line-height: 1;
  }
  .brand-tag {
    font-size: 16px; font-weight: 400; letter-spacing: 6px; margin-top: 14px; line-height: 1;
  }
  .contact {
    position: absolute; left: 606px; top: 36px;
    border-left: 1.5px solid var(--rule);
    padding-left: 12px;
    font-size: 12px; line-height: 18.5px; color: var(--ink);
  }
  .contact li { list-style: none; display: flex; align-items: center; gap: 5px; }
  .contact svg { width: 10px; height: 10px; fill: var(--ink-soft); }
  .letter-body {
    position: absolute; left: 71px; top: 302px; width: 693px;
  }
  .salutation { font-weight: 700; font-size: 14.5px; margin-bottom: 20px; }
  .letter-body p.copy {
    font-size: 16.2px; line-height: 24.5px; text-align: justify;
    margin-bottom: 18px;
  }
  .closing { font-size: 19px; margin-top: 24px; }
  .signature {
    font-family: "Dancing Script", cursive;
    font-weight: 700; font-size: 32px; margin-top: 4px; color: var(--ink);
  }
  .footer-band {
    position: absolute; left: 0; top: 980px; width: 835px; height: 100px;
  }
  .address {
    position: absolute; left: 70px; top: 1026px;
    font-style: normal;
    color: var(--on-band); font-size: 14px; line-height: 20px;
  }
  .address .line1 { display: flex; align-items: center; gap: 5px; }
  .address svg { width: 12px; height: 12px; }
  .address .line2 { padding-left: 17px; }
</style>
</head>
<body>
<main class="letterhead">
  <header>
    <div class="brand">
      <div class="brand-name">BRIGHTFOLD</div>
      <div class="brand-tag">HARBOR LIMITED</div>
    </div>
    <ul class="contact">
      <li><svg viewBox="0 0 10 10"><path d="M2 0.5 L3.6 0.5 L4.2 2.8 L3 3.6 Q4 5.8 6.4 7 L7.2 5.8 L9.5 6.4 L9.5 8 Q9 9.6 7.5 9.5 Q1 8.5 0.5 2 Q0.5 0.8 2 0.5Z"/></svg>012-345-6789</li>
      <li><svg viewBox="0 0 10 10"><path d="M0.5 2.5 H9.5 V8.5 H0.5Z M1 3 L5 6 L9 3" stroke="#fff" stroke-width=".8"/></svg>info@brightfoldharbor.com</li>
      <li><svg viewBox="0 0 10 10"><circle cx="5" cy="5" r="4.3" fill="none" stroke="#555" stroke-width=".9"/><path d="M0.7 5 H9.3 M5 0.7 Q2.5 5 5 9.3 M5 0.7 Q7.5 5 5 9.3" fill="none" stroke="#555" stroke-width=".8"/></svg>www.brightfoldharbor.com</li>
    </ul>
  </header>

  <section class="letter-body">
    <p class="salutation">Dear Mr. Lorem,</p>
    <p class="copy">Lorem ipsum dolor sit amet, consectetuer adipiscing elit, sed diam nonummy nibh euismod tincidunt ut laoreet dolore magna aliquam erat volutpat. Ut wisi enim ad minim veniam, quis nostrud exerci tation ullamcorper suscipit lobortis nisl ut aliquip ex ea commodo consequat. Duis autem vel eum iriure dolor in hendiusto odio dignissim qui blandit praesent luptatum zzril delenit augue duis dolore te feugait nulla facilisi.</p>
    <p class="copy">Lorem ipsum dolor sit amet, consectetuer adipiscing elit, sed diam nonummy nibh euismod tincidunt ut laoreet dolore magna aliquam erat volutpat. Ut wisi enim ad minim veniam, quis nostrud exerci tation ullamcorper suscipit lobortis nisl ut aliquip ex ea commodo consequat. Duis autem vel eum iriure dolor in hendiusto odio dignissim qui blandit praesent luptatum zzril delenit augue duis dolore te feugait nulla facilisi.</p>
    <p class="copy">Lorem ipsum dolor sit amet, consectetuer adipiscing elit, sed diam nonummy nibh euismod tincidunt ut laoreet dolore magna aliquam erat volutpat. Ut wisi enim ad minim veniam, quis nostrud exerci tation ullamcorper suscipit lobortis nisl ut aliquip ex ea commodo consequat. Duis autem vel eum iriure dolor in hendiusto odio dignissim qui blandit praesent luptatum zzril delenit augue duis dolore te feugait nulla facilisi.</p>
    <p class="closing">Sincerely Your,</p>
    <p class="signature">Your Name</p>
  </section>

  <svg class="footer-band" viewBox="0 0 835 100" preserveAspectRatio="none" aria-hidden="true">
    <path class="band-fill" d="M0,50 C150,23 330,14 470,38 C620,50 760,28 835,7 L835,100 L0,100Z" fill="var(--band)"/>
    <path class="band-upper-wedge" d="M480,40 C620,52 760,28 835,7 L835,22 C760,42 620,57 480,43Z" fill="var(--swoosh)"/>
    <path class="band-curve" d="M0,42 C150,15 330,6 470,30 C580,50 700,64 835,66" fill="none" stroke="var(--swoosh)" stroke-width="7"/>
    <path class="band-line" d="M0,48 C150,21 330,12 470,36 C580,56 700,70 835,72" fill="none" stroke="#fff" stroke-width="2.2"/>
    <path class="band-line" d="M520,64 C650,84 760,86 835,80" fill="none" stroke="#fff" stroke-width="2.2"/>
  </svg>

  <address class="address">
    <div class="line1">
      <svg viewBox="0 0 12 12"><path d="M6 0.8 A4 4 0 0 1 10 4.8 C10 7.5 6 11.2 6 11.2 C6 11.2 2 7.5 2 4.8 A4 4 0 0 1 6 0.8Z" fill="none" stroke="#fff" stroke-width="1.2"/><circle cx="6" cy="4.8" r="1.4" fill="#fff"/></svg>
      Street Name, City Name
    </div>
    <div class="line2">Zipcode-012345</div>
  </address>
</main>
</body>
</html>
```